New Company Business Card design

Looking for a corporate looking business card utilising my new logo design - the logo i would like embossed as one option and flat as another - simplistic but stylish - less is more - we are an import export business launching into the market - i would like a couple of options as main background - Grey or Black

```html
<!DOCTYPE html>
<html lang="en">
<head>
<meta charset="utf-8">
<title>Corvane Trade Group – Business Card</title>
<link href="https://fonts.googleapis.com/css2?family=Roboto:wght@400;500;700&family=Roboto+Condensed:wght@500;700&display=swap" rel="stylesheet">
<style>
  :root {
    --page-bg: #e9e7e3;
    --card-light: #f5f5f4;
    --card-dark: #1b1c1e;
    --brand-blue: #1876c2;
    --text-grey: #5a5a5a;
    --tagline-grey: #6e6e6e;
    --faint-blue: #dbe7f1;
    --white: #ffffff;
  }
  * { box-sizing: border-box; margin: 0; padding: 0; }
  html, body { width: 1200px; height: 960px; overflow: hidden; }
  body {
    background: var(--page-bg);
    position: relative;
    font-family: "Roboto", Arial, sans-serif;
  }
  .card {
    position: absolute;
    width: 600px;
    height: 342px;
    overflow: hidden;
    box-shadow: 0 3px 8px rgba(0,0,0,0.25);
  }
  .card--front { left: 314px; top: 113px; background: var(--card-light); }
  .card--back { left: 311px; top: 472px; background: var(--card-dark); }

  .front-decor {
    position: absolute;
    left: 325px; top: 118px;
    width: 330px; height: 330px;
    border-radius: 50%;
    background: var(--faint-blue);
    opacity: 0.55;
  }
  .brand {
    position: absolute;
    left: 40px; top: 60px;
    width: 236px;
    display: flex; align-items: center; gap: 8px;
  }
  .brand__dot {
    width: 16px; height: 16px; border-radius: 50%;
    background: var(--brand-blue); flex: none;
  }
  .brand__name {
    font-family: "Roboto", Arial, sans-serif;
    font-weight: 500;
    font-size: 21px;
    color: var(--brand-blue);
    white-space: nowrap;
  }
  .brand__tagline {
    position: absolute;
    left: 40px; top: 148px;
    width: 236px;
    text-align: center;
    font-size: 8px;
    letter-spacing: 1.6px;
    text-transform: uppercase;
    color: var(--tagline-grey);
    border-top: 1px solid #9a9a9a;
    padding-top: 3px;
  }
  .address {
    position: absolute;
    left: 39px; top: 195px;
    font-size: 14px; line-height: 19px;
    color: var(--text-grey);
  }
  .contacts {
    position: absolute;
    left: 39px; top: 239px;
    list-style: none;
    font-size: 14px; line-height: 19px;
    color: var(--text-grey);
  }
  .contacts li { display: flex; align-items: center; gap: 8px; }
  .contacts svg { width: 14px; height: 14px; fill: var(--brand-blue); flex: none; }
  .person {
    position: absolute;
    right: 30px; top: 232px;
    text-align: right;
    font-family: "Roboto Condensed", Arial, sans-serif;
  }
  .person__name { font-size: 21px; font-weight: 700; color: var(--brand-blue); line-height: 24px; }
  .person__role { font-size: 14px; font-weight: 500; color: var(--text-grey); line-height: 18px; }

  .back-brand {
    position: absolute;
    left: 0; right: 0; top: 130px;
    display: flex; justify-content: center; align-items: center; gap: 14px;
  }
  .back-brand__dot { width: 30px; height: 30px; border-radius: 50%; background: var(--white); }
  .back-brand__name {
    font-weight: 500; font-size: 44px; color: var(--white); white-space: nowrap;
  }
  .website {
    position: absolute;
    left: 0; right: 0; top: 288px;
    text-align: center;
    font-size: 14px; letter-spacing: 2px;
    color: var(--white);
  }
</style>
</head>
<body>
  <section class="card card--front">
    <div class="front-decor" aria-hidden="true"></div>
    <div class="brand">
      <span class="brand__dot"></span>
      <span class="brand__name">Corvane Trade Group</span>
    </div>
    <p class="brand__tagline">Worldwide supply for every market</p>
    <address class="address" style="font-style:normal">
      214 Harbor View Road<br>Portland, Maine 04101
    </address>
    <ul class="contacts">
      <li><svg viewBox="0 0 24 24"><path d="M6.6 10.8a15.1 15.1 0 0 0 6.6 6.6l2.2-2.2a1 1 0 0 1 1-.25 11.4 11.4 0 0 0 3.6.57 1 1 0 0 1 1 1V20a1 1 0 0 1-1 1A17 17 0 0 1 3 4a1 1 0 0 1 1-1h3.5a1 1 0 0 1 1 1c0 1.25.2 2.45.57 3.57a1 1 0 0 1-.25 1z"/></svg>207 555 0148</li>
      <li><svg viewBox="0 0 24 24"><path d="M7 1h10a2 2 0 0 1 2 2v18a2 2 0 0 1-2 2H7a2 2 0 0 1-2-2V3a2 2 0 0 1 2-2zm0 3v14h10V4zm5 15.5a1.2 1.2 0 1 0 0 2.4 1.2 1.2 0 0 0 0-2.4z"/></svg>207 555 0193</li>
      <li><svg viewBox="0 0 24 24"><path d="M6 2h12v5H6zM3 8h18a2 2 0 0 1 2 2v7h-4v5H5v-5H1v-7a2 2 0 0 1 2-2zm4 8v4h10v-4z"/></svg>207 555 0162</li>
      <li><svg viewBox="0 0 24 24"><path d="M2 5h20v2l-10 6L2 7zm0 4.3 10 6 10-6V19H2z"/></svg>hello@corvanetrade.com</li>
    </ul>
    <div class="person">
      <p class="person__name">DANIEL HART</p>
      <p class="person__role">CEO/FOUNDER</p>
    </div>
  </section>

  <section class="card card--back">
    <div class="back-brand">
      <span class="back-brand__dot"></span>
      <span class="back-brand__name">Corvane Trade Group</span>
    </div>
    <p class="website">www.corvanetradegroup.com</p>
  </section>
</body>
</html>
```